Clean & Inspiring Web Design Project

Larkspur Prototype Studio, LLC (also known as LP-Studio) is a company which provides 3D printing services and products. The emphasis is on making these products and services available to the mass-market - customers and users who may or may not have prior experience with 3D printing and/or rapid prototyping technologies. We are a start-up company, looking to build a clean and creativity inspiring brand - our site must encourage visitor to engage and make something. Our aim is to help take mere ideas and turn them into tangible items. We want to show a fusion of ideas (e.g. pencil sketches on graph paper) with design tools (e.g. CAD and drafting software) and rapid prototyping (e.g. TinkNod 3D printers, Stereolithography Machines, etc.). We would like the website to appear professional but at the same time easy to navigate and a good balance between text and pictures. The final design should inspire customers to nurture their ideas into real products and communicate our services to our customers. Our site should have the feel of a vibrant social community with the added benefit of tangible physical creations.

Target Market(s)

People with great ideas that need to be designed into a real product

Industry/Entity Type

Printing

Requirements
Must have
• - Website design should include 2 layouts - one for a "landing page" and one for a "content page"
- Website design must incorporate attached company logo (or derivative of this logo)
- Website design should incorporate the menu options shown in the attached PDF UI concept (UI does not necessarily need to look like the provided concept, just include all the clickable elements)
- Website design must portray an innovative and cooperative design environment with a look-and-feel that appeals to both amateur and professional designers.
- Please include pictures, illustrations and photographs (as needed) related to 3D printing, CAD design, conventional drafting, engineering and manufacturing industries.
- Design should support scaling to multiple screen sizes, from tablet computers (e.g. Slabix) to very large screen PCs.
- Design should include Username & Password fields for login or a button to pull up a login popup.
Nice to have
• - Website design could include "Invent", "Make", "Produce" and "Buy" options that slowly cycle through - with appropriate photos / graphics. These "menu options" would also be mouse-over enabled to switch into the appropriate context as the cursor enters that region (e.g. mouse over the "Invent" text would bring up page 2, etc.). (See attached Original UI Thoughts)
Should not have
• Requirements - Should Not Have:
- Website design should not portray a service that is very expensive or complicated - we are a reasonably priced service meant to be friendly with amateur inventors
- Website design should not be overly complicated - please keep it reasonably simple
- Website design should not be overly trendy
- Website design should not use more than 2 font styles, gaudy fonts, etc.
- Website design should not be "campy" or "tacky" - playful is ok, but please keep it elegant
- Website design should not be overly masculine or feminine - we will have both women and men as customers

```html
<!DOCTYPE html>
<html lang="en">
<head>
<meta charset="utf-8">
<title>LP-Studio — About us</title>
<link rel="stylesheet" href="https://fonts.googleapis.com/css2?family=Ubuntu:wght@400;500&family=Carlito:wght@400;700&display=swap">
<style>
  :root {
    --cream: #fffbd0;
    --teal: #6a9d9e;
    --teal-deep: #5b9294;
    --teal-ink: #3b6768;
    --panel-ink: #2d5a5e;
    --brand-blue: #1b5f9c;
    --slate: #595959;
    --footer: #424242;
    --white: #ffffff;
    --orange-top: #f6b385;
    --orange-bottom: #e07a45;
    --nav-ink: #3a3a3a;
  }
  * { box-sizing: border-box; margin: 0; padding: 0; }
  html, body { width: 1200px; height: 900px; overflow: hidden; }
  body {
    position: relative;
    background: var(--cream);
    font-family: "Carlito", "Calibri", sans-serif;
  }
  .abs { position: absolute; }

  /* Header */
  .brand { left: 24px; top: 14px; display: flex; align-items: center; gap: 14px; }
  .brand-mark { width: 66px; height: 66px; background: var(--brand-blue); }
  .brand-name { font-family: "Ubuntu", sans-serif; font-weight: 500; font-size: 34px; color: var(--brand-blue); }

  .main-nav a {
    position: absolute; top: 24px;
    font-family: "Ubuntu", sans-serif; font-size: 33px; color: var(--nav-ink); text-decoration: none;
  }
  .account-btn {
    position: absolute; left: 1034px; width: 139px; height: 30px;
    background: linear-gradient(#8cbcbc, #5f9596);
    border: 1px solid #4f8485;
    color: #1f4c68; font-family: "Ubuntu", sans-serif; font-size: 22px;
    display: flex; align-items: center; justify-content: center; gap: 4px;
  }
  .account-btn.login { top: 14px; }
  .account-btn.shop { top: 51px; }

  /* Section tabs */
  .tab-band { left: 0; top: 138px; width: 1200px; height: 72px; background: var(--teal); }
  .tab-active {
    left: 0; top: 138px; width: 245px; height: 72px; background: var(--slate);
    color: var(--white); font-family: "Ubuntu", sans-serif; font-size: 40px;
    display: flex; align-items: center; justify-content: center;
  }
  .tab {
    top: 148px; transform: translateX(-50%);
    font-family: "Ubuntu", sans-serif; font-size: 33px; color: var(--teal-ink);
  }

  /* Content panel */
  .panel {
    left: 0; top: 240px; width: 1200px; height: 357px;
    background:
      radial-gradient(circle at 22% 10%, rgba(255,255,255,0.22), transparent 22%),
      radial-gradient(circle at 80% 40%, rgba(255,255,255,0.18), transparent 28%),
      radial-gradient(circle at 55% 70%, rgba(255,255,255,0.10), transparent 30%),
      linear-gradient(90deg, var(--teal-deep), #74a9aa 60%, var(--teal-deep));
  }
  .panel-pointer { left: 0; top: 209px; }
  .panel-title {
    left: 20px; top: 256px;
    font-family: "Ubuntu", sans-serif; font-size: 33px; color: var(--panel-ink); letter-spacing: -1px;
  }
  .panel-copy {
    left: 20px; top: 309px; width: 690px;
    font-size: 24px; line-height: 31.5px; color: var(--panel-ink);
  }
  .feature-art {
    left: 860px; top: 250px; width: 290px; height: 230px;
    border: 3px solid rgba(255,255,255,0.8);
    background: radial-gradient(circle at 40% 45%, #e9dfc4, #d7c69d 55%, #c9b88d);
    box-shadow: 0 0 14px rgba(255,255,255,0.5);
  }
  .bios-btn {
    left: 861px; top: 497px; width: 288px; height: 64px;
    background: linear-gradient(var(--orange-top), var(--orange-bottom));
    border: 2px solid #2d6e9e;
    display: flex; align-items: center; gap: 16px; padding-left: 16px;
    font-family: "Ubuntu", sans-serif; font-size: 33px; color: var(--teal-ink);
  }
  .bios-btn .mark { width: 42px; height: 42px; background: var(--brand-blue); }

  /* Footer */
  .footer { left: 0; top: 627px; width: 1200px; height: 273px; background: var(--footer); }
  .promo-heading, .promo-link, .promo-note, .footer-nav a {
    position: absolute; color: var(--white); font-size: 20px; white-space: nowrap;
  }
  .promo-heading { top: 638px; }
  .promo-link { display: flex; align-items: center; gap: 10px; top: 788px; }
  .promo-note { left: 1071px; top: 704px; transform: translateX(-50%); text-align: center; line-height: 26px; }
  .promo-img { position: absolute; }
  .arrow { width: 36px; height: 36px; }

  .social-mark { left: 37px; top: 853px; width: 38px; height: 36px; background: #6fb3d6; border-radius: 4px; }
  .footer-nav a { top: 866px; transform: translateX(-50%); text-decoration: none; }
</style>
</head>
<body>

<!-- Header -->
<header>
  <div class="abs brand"><span class="brand-mark"></span><span class="brand-name">LP-Studio</span></div>
  <nav class="main-nav">
    <a style="left:302px">why LP</a>
    <a style="left:458px">dreamer</a>
    <a style="left:640px">maker</a>
    <a style="left:792px">producer</a>
  </nav>
  <a class="account-btn login">login</a>
  <a class="account-btn shop">
    <svg width="22" height="20" viewBox="0 0 22 20" aria-hidden="true">
      <path d="M1 2h4l3 11h10l3-8H7" fill="none" stroke="#1f4c68" stroke-width="2"/>
      <circle cx="9" cy="17" r="2" fill="#1f4c68"/><circle cx="17" cy="17" r="2" fill="#1f4c68"/>
    </svg>shop</a>
</header>

<!-- Section tabs -->
<div class="abs tab-band"></div>
<div class="abs tab-active">about us</div>
<span class="abs tab" style="left:355px">dream</span>
<span class="abs tab" style="left:577px">make</span>
<span class="abs tab" style="left:823px">produce</span>
<span class="abs tab" style="left:1072px">sell</span>

<!-- Content panel -->
<section class="abs panel"></section>
<svg class="abs panel-pointer" width="1200" height="32" viewBox="0 0 1200 32" aria-hidden="true">
  <polygon points="333,0 372,0 396,32 310,32" fill="var(--teal-deep)"/>
</svg>
<h1 class="abs panel-title">TITLE TEXT</h1>
<p class="abs panel-copy">Lorem ipsum dolor sit amet, consectetur adipisicing elit, sed do eiusmod tempor incididunt ut labore et dolore magna aliqua. Ut enim ad minim veniam, quis nostrud exercitation ullamco laboris nisi ut aliquip ex ea commodo consequat. Duis aute irure dolor in reprehenderit in voluptate velit esse cillum dolore eu fugiat nulla pariatur. Excepteur sint occaecat cupidatat non proident, sunt in culpa qui officia deserunt mollit anim id est laborum.</p>
<div class="abs feature-art" role="img" aria-label="Illustration of a seedling growing from a head in profile, symbolising an idea taking root"></div>
<a class="abs bios-btn"><span class="mark"></span>team LP bios</a>

<!-- Footer -->
<footer class="abs footer"></footer>

<span class="promo-heading" style="left:37px">find unique items at the LP store</span>
<div class="promo-img" style="left:21px;top:682px;width:134px;height:101px;background:radial-gradient(circle,#b89a5a,#6a5127 60%,#1e1a12)" role="img" aria-label="Photo of an intricate 3D printed sculpture"></div>
<div class="promo-img" style="left:192px;top:682px;width:130px;height:101px;background:linear-gradient(135deg,#d8c6a8,#7a4e2c 55%,#b99a78)" role="img" aria-label="Photo of printed high-heeled shoes"></div>
<span class="promo-link" style="left:77px">see more products
  <svg class="arrow" viewBox="0 0 36 36" aria-hidden="true"><circle cx="18" cy="18" r="16" fill="none" stroke="#fff" stroke-width="2.5"/><path d="M15 10l8 8-8 8" fill="none" stroke="#fff" stroke-width="3"/></svg></span>

<span class="promo-heading" style="left:576px;transform:translateX(-50%)">purchase LP printers</span>
<div class="promo-img" style="left:508px;top:673px;width:134px;height:103px;background:linear-gradient(#f4f4f4,#e8a84a 40%,#f0f0f0 75%,#dcdcdc)" role="img" aria-label="Photo of a desktop 3D printer with an orange cover"></div>
<span class="promo-link" style="left:507px">find more
  <svg class="arrow" viewBox="0 0 36 36" aria-hidden="true"><circle cx="18" cy="18" r="16" fill="none" stroke="#fff" stroke-width="2.5"/><path d="M15 10l8 8-8 8" fill="none" stroke="#fff" stroke-width="3"/></svg></span>

<span class="promo-heading" style="left:808px">read latest news in our blog</span>
<div class="promo-img" style="left:840px;top:673px;width:132px;height:103px;background:linear-gradient(135deg,#e9e9e9,#3a3a3a 45%,#e07030 65%,#d8d8d8)" role="img" aria-label="Photo of assorted colourful printed parts"></div>
<span class="promo-note">newest products<br>and accesories</span>
<span class="promo-link" style="left:855px">read more
  <svg class="arrow" viewBox="0 0 36 36" aria-hidden="true"><circle cx="18" cy="18" r="16" fill="none" stroke="#fff" stroke-width="2.5"/><path d="M15 10l8 8-8 8" fill="none" stroke="#fff" stroke-width="3"/></svg></span>

<span class="abs social-mark" aria-label="social link"></span>
<nav class="footer-nav">
  <a style="left:204px">home</a>
  <a style="left:384px">contact</a>
  <a style="left:576px">franchise</a>
  <a style="left:795px">distributors</a>
  <a style="left:990px">cart</a>
</nav>

</body>
</html>
```